IT Network Consultancy - Business Card

t4 linkways is a IT network consultancy based in London. We're looking for a smart, modern and professional business card design. Our website is here: www.t4linkways.co.uk

Key things that should be included on the card (with examples):

Company Logo
Name
Position / Job Title: Network Consultant
Mobile Phone Number: +44 (0) 7700 900418
Land Line: +44 (0) 1632 960274
Email Address: name@t4linkways.co.uk
Web Site URL: www.t4linkways.co.uk

Target Market(s)

Large enterprise / global companies / corporates

Industry/Entity Type

Business

Requirements
Must have
• Incorporate our logo - which is attached to the project. They are in AI format (can be opened in Inkscape).

The design should be double sided and fit on a UK standard 85mm × 55mm card and be in a format that retains the quality when printed.
Nice to have
• The project does not have to conform to the colour of our website but this should give you inspiration of the style we like.
Should not have
• Bright colours. Pictures are not necessary.

```html
<!DOCTYPE html>
<html lang="en">
<head>
<meta charset="utf-8">
<title>t4 linkways – Business Card</title>
<link rel="stylesheet" href="https://fonts.googleapis.com/css2?family=Montserrat:wght@300&family=PT+Sans:wght@400;700&display=swap">
<style>
  :root {
    --page: #fdfdfd;
    --card: #262626;
    --ink: #ffffff;
    --accent: #8f9a9c;
  }
  * { margin: 0; padding: 0; box-sizing: border-box; }
  html, body {
    width: 1200px;
    height: 846px;
    overflow: hidden;
    background: var(--page);
  }
  .sheet {
    position: relative;
    width: 1200px;
    height: 846px;
  }
  .card {
    position: absolute;
    top: 248px;
    width: 486px;
    height: 313px;
    background: var(--card);
    overflow: hidden;
    color: var(--ink);
  }
  .card--front { left: 78px; }
  .card--back  { left: 635px; }

  /* Front */
  .brand {
    position: absolute;
    right: 28px;
    bottom: 24px;
    display: flex;
    align-items: center;
    gap: 12px;
  }
  .brand__dot {
    width: 22px;
    height: 22px;
    border-radius: 50%;
    background: var(--accent);
  }
  .brand__name {
    font-family: "Montserrat", sans-serif;
    font-weight: 300;
    font-size: 29px;
    letter-spacing: 2px;
    text-transform: uppercase;
    color: var(--ink);
    line-height: 1;
  }

  /* Back */
  .person {
    position: absolute;
    left: 35px;
    top: 32px;
  }
  .person__name {
    font-family: "Montserrat", sans-serif;
    font-weight: 300;
    font-size: 19px;
    letter-spacing: 1.5px;
    text-transform: uppercase;
    line-height: 1;
  }
  .person__role {
    margin-top: 6px;
    font-family: "PT Sans", sans-serif;
    font-weight: 700;
    font-size: 14.5px;
    line-height: 1;
  }
  .contact {
    position: absolute;
    left: 35px;
    top: 94px;
    font-family: "PT Sans", sans-serif;
    font-size: 15px;
    line-height: 19.4px;
    list-style: none;
  }
  .contact__item { display: flex; }
  .contact__label {
    width: 26px;
    font-weight: 700;
  }
  .monogram {
    position: absolute;
    right: -14px;
    bottom: -52px;
    font-family: "PT Sans", sans-serif;
    font-weight: 700;
    font-size: 230px;
    line-height: 1;
    letter-spacing: -8px;
    color: var(--ink);
    text-transform: uppercase;
  }
</style>
</head>
<body>
<main class="sheet">
  <section class="card card--front" aria-label="Card front">
    <div class="brand">
      <span class="brand__dot"></span>
      <span class="brand__name">t4 linkways</span>
    </div>
  </section>

  <section class="card card--back" aria-label="Card back">
    <div class="person">
      <h1 class="person__name">Daniel Hart</h1>
      <p class="person__role">Network Consultant</p>
    </div>
    <ul class="contact">
      <li class="contact__item"><span class="contact__label">M.</span><span>+44 (0) 7700 900418</span></li>
      <li class="contact__item"><span class="contact__label">P.</span><span>+44 (0) 1632 960274</span></li>
      <li class="contact__item"><span class="contact__label">E.</span><span>daniel@t4linkways.co.uk</span></li>
      <li class="contact__item"><span class="contact__label">W.</span><span>www.t4linkways.co.uk</span></li>
    </ul>
    <div class="monogram" aria-hidden="true">t4</div>
  </section>
</main>
</body>
</html>
```